Bingo Night

Willowmere Terraces is an Assisted Living Facility. We have 34 residents currently living in our facility. We provide care for elderly patients that need a slightly higher level of care than what can be provided at home. We are sending out this invitation to people in the surrounding community for Bingo night March 19, 2014 @ 6:00pm. The colors we would like to use are gold & maroon. Our address is 2947 W 38th St Tulsa, OK 74107. 918-562-3049. Also, the phrase "open to the public" should be incorporated on both sides.
Updates

Target Market(s)

Men and women between the ages of 50-90 years old.

Industry/Entity Type

Community

Font styles to use
Serif
Script

Requirements
Must have
• At least 4 pictures provided, our address, time of event, and phone number.

```html
<!DOCTYPE html>
<html lang="en">
<head>
<meta charset="utf-8">
<title>Bingo Night – Willowmere Terraces</title>
<link rel="stylesheet" href="https://fonts.googleapis.com/css2?family=Sorts+Mill+Goudy:ital@0;1&display=swap">
<style>
  :root {
    --maroon: #7c1116;
    --maroon-deep: #4e070b;
    --maroon-light: #9a1a1f;
    --gold: #d6ae5c;
    --gold-light: #e8c877;
    --gold-dark: #b68a3a;
    --ink: #741418;
    --shadow: rgba(20, 0, 0, 0.55);
  }
  * { margin: 0; padding: 0; box-sizing: border-box; }
  html, body { width: 1200px; height: 900px; overflow: hidden; }
  body { font-family: "Sorts Mill Goudy", Georgia, serif; }

  .invitation {
    position: relative;
    width: 1200px;
    height: 900px;
    overflow: hidden;
    background:
      radial-gradient(ellipse 520px 380px at 560px 520px, rgba(170, 30, 36, 0.55), transparent 70%),
      radial-gradient(ellipse 700px 300px at 1000px 120px, rgba(150, 24, 30, 0.4), transparent 70%),
      linear-gradient(180deg, var(--maroon) 0%, var(--maroon) 55%, var(--maroon-deep) 100%);
  }

  .headline {
    position: absolute;
    color: var(--gold);
    text-shadow: 3px 4px 5px var(--shadow);
    line-height: 1;
    white-space: nowrap;
  }
  .headline--welcome { left: 26px; top: 42px; font-size: 122px; letter-spacing: 1px; }
  .headline--event { left: 68px; top: 160px; font-size: 58px; }

  .gold-band {
    position: absolute;
    left: 0; top: 233px;
    width: 1200px; height: 19px;
    background: linear-gradient(180deg, var(--gold-light), var(--gold-dark));
    box-shadow: 0 3px 4px var(--shadow);
  }

  .date-badge { position: absolute; left: 548px; top: 108px; width: 460px; height: 206px; }
  .date-badge__text {
    position: absolute;
    left: 0; top: 48px; width: 440px;
    text-align: center;
    color: var(--ink);
    font-size: 44px;
    line-height: 56px;
  }

  .contact {
    position: absolute;
    right: 34px; top: 30px;
    text-align: right;
    color: var(--gold);
    font-size: 30px;
    line-height: 37.5px;
    text-shadow: 2px 3px 4px var(--shadow);
  }

  .photo {
    position: absolute;
    border: 6px solid var(--gold);
    border-radius: 9px;
    box-shadow: 4px 6px 10px var(--shadow);
  }
  .photo--garden {
    left: 72px; top: 296px; width: 274px; height: 220px;
    background: linear-gradient(170deg, #c9c6bd 0%, #6f8c4a 35%, #4c6a34 65%, #8f8a7c 100%);
  }
  .photo--lobby {
    left: 616px; top: 345px; width: 174px; height: 165px;
    background: linear-gradient(180deg, #e6d9b8 0%, #8a5a36 45%, #5a4a4c 75%, #6b5f63 100%);
  }
  .photo--dining {
    left: 334px; top: 506px; width: 293px; height: 281px;
    background: linear-gradient(160deg, #d9c3ab 0%, #c9a98a 40%, #6a5146 75%, #4a3e3c 100%);
  }
  .photo--pet-visit {
    left: 782px; top: 505px; width: 348px; height: 332px;
    background: linear-gradient(150deg, #c9a67a 0%, #b7957a 35%, #8a7f7c 65%, #5b4a4e 100%);
  }

  .tagline {
    position: absolute;
    left: 46px; top: 812px;
    color: var(--gold);
    font-style: italic;
    font-size: 50px;
    line-height: 1;
    text-shadow: 2px 3px 4px var(--shadow);
  }
</style>
</head>
<body>
  <main class="invitation">
    <h1 class="headline headline--welcome">Welcome</h1>
    <p class="headline headline--event">to Bingo Night</p>

    <div class="gold-band"></div>

    <div class="date-badge">
      <svg width="460" height="206" viewBox="0 0 460 206" aria-hidden="true">
        <defs>
          <linearGradient id="badgeGold" x1="0" y1="0" x2="0" y2="1">
            <stop offset="0" stop-color="#e2bf6c"/>
            <stop offset="1" stop-color="#cfa352"/>
          </linearGradient>
        </defs>
        <ellipse cx="232" cy="106" rx="220" ry="94" fill="#2a0406" opacity="0.7"/>
        <ellipse cx="222" cy="98" rx="220" ry="94" fill="url(#badgeGold)"/>
      </svg>
      <p class="date-badge__text">March 19, 2014<br>at 6:00pm</p>
    </div>

    <address class="contact" style="font-style: normal;">
      2947 W 38th St Tulsa<br>
      OK 74107<br>
      918-562-3049
    </address>

    <div class="photo photo--garden" role="img" aria-label="Garden with flowering crape myrtle, pine trees and a stone waterfall"></div>
    <div class="photo photo--lobby" role="img" aria-label="Lobby with fireplace, plants and patterned carpet"></div>
    <div class="photo photo--dining" role="img" aria-label="Dining room with chef statue holding a menu board beside a piano"></div>
    <div class="photo photo--pet-visit" role="img" aria-label="Resident petting a visiting therapy dog in a sitting room"></div>

    <p class="tagline">open to the public</p>
  </main>
</body>
</html>
```